Hadley & Partners, LLC Business Card 2016

We need a new business card design for a very important trade show coming up.

We are a compliance Consulting Firm. Our clients are stock brokerage firms and investment advisers.

I would like our logo on both sides of the card.

Info in the front of the card shold include:

Logo
First & Last Name
Title
Office #
Cell #
Email
Company Address (42 W. Calloway St., Suite 300 Pasadena, CA 91417

Back of the card should include the logo and url: www.hadleypartnersgroup.com

Target Market(s)

Stock Brokerage Firms and Investment Advisers

Industry/Entity Type

Financial Service

Contact Information for Business Card

Marcus J. Pellew
President
42 W. Calloway St., Suite 300
Pasadena, CA 91417
O 626.555.0147 ext. 204
C 818.555.0193
Email: marcus@hadleypartnersgroup.com
www.hadleypartnersgroup.com

Requirements
Nice to have
• The back of the card could be black with the logo with the white letters.
• I do want the front of the card to at least have the color logo with the black "Hadley & Partners Lettering.

```html
<!DOCTYPE html>
<html lang="en">
<head>
<meta charset="utf-8">
<title>Hadley &amp; Partners — Business Card</title>
<link rel="stylesheet" href="https://fonts.googleapis.com/css2?family=Montserrat:wght@400;500;600;700&display=swap">
<style>
  :root {
    --canvas: #e9e7e4;
    --card-dark: #231f20;
    --brand-red: #d92629;
    --white: #ffffff;
    --panel-grey: #b9bbbd;
    --ink: #231f20;
    --ink-soft: #3a3637;
  }
  * { margin: 0; padding: 0; box-sizing: border-box; }
  html, body { width: 1200px; height: 892px; overflow: hidden; }
  body {
    background: var(--canvas);
    font-family: "Montserrat", sans-serif;
    position: relative;
  }
  .card {
    position: absolute;
    left: 250px;
    width: 700px;
    height: 400px;
    overflow: hidden;
    box-shadow: 0 6px 18px rgba(0,0,0,0.18);
  }
  .card__art { position: absolute; inset: 0; width: 700px; height: 400px; }

  /* Front */
  .card--front { top: 30px; background: var(--card-dark); }
  .contact-list { position: absolute; list-style: none; }
  .contact-list li {
    display: flex; align-items: center; gap: 10px;
    color: var(--white); font-size: 14px; font-weight: 400;
    letter-spacing: 0.2px; line-height: 28px; white-space: nowrap;
  }
  .contact-list--phones { left: 34px; top: 34px; }
  .contact-list--mail { left: 34px; bottom: 28px; }
  .contact-icon { width: 18px; height: 18px; flex: none; }

  .wordmark {
    position: absolute; display: flex; align-items: center; gap: 12px;
    font-weight: 700; letter-spacing: 1.5px; text-transform: uppercase;
  }
  .wordmark__square { width: 26px; height: 26px; background: var(--brand-red); flex: none; }
  .wordmark--front { right: 40px; top: 176px; font-size: 24px; color: var(--white); }
  .wordmark--back { left: 56px; top: 54px; font-size: 30px; color: var(--ink); }

  .holder { position: absolute; right: 40px; bottom: 36px; text-align: right; color: var(--white); }
  .holder__name { font-size: 18px; font-weight: 700; }
  .holder__title { font-size: 15px; font-weight: 400; margin-top: 3px; }

  /* Back */
  .card--back { top: 462px; background: var(--white); }
  .site-url {
    position: absolute; right: 44px; bottom: 40px;
    font-size: 20px; font-weight: 500; color: var(--ink-soft); letter-spacing: 0.4px;
  }
</style>
</head>
<body>

<section class="card card--front" aria-label="Business card front">
  <svg class="card__art" viewBox="0 0 700 400" aria-hidden="true">
    <path d="M0,130 C170,100 290,150 360,240 C420,310 475,380 600,400 L0,400 Z" fill="#ffffff"/>
    <path d="M0,146 C160,118 276,166 342,250 C400,320 450,385 570,400 L0,400 Z" fill="#d92629"/>
  </svg>

  <ul class="contact-list contact-list--phones">
    <li>
      <svg class="contact-icon" viewBox="0 0 20 20"><circle cx="10" cy="10" r="10" fill="#ffffff"/><path d="M7 5l2 2-1 1.5c.6 1.4 1.7 2.5 3.1 3.1L12.5 10.6l2 2-1.3 1.6C9.5 14 6 10.5 5.8 6.3z" fill="#231f20"/></svg>
      818.555.0193
    </li>
    <li>
      <svg class="contact-icon" viewBox="0 0 20 20"><circle cx="10" cy="10" r="10" fill="#ffffff"/><rect x="5" y="8" width="10" height="6" rx="1" fill="#231f20"/><rect x="6" y="5.5" width="8" height="2.5" rx="1" fill="#231f20"/></svg>
      626.555.0147 ext. 204
    </li>
  </ul>

  <div class="wordmark wordmark--front"><span class="wordmark__square"></span>Hadley &amp; Partners</div>

  <ul class="contact-list contact-list--mail">
    <li>
      <svg class="contact-icon" viewBox="0 0 20 20"><circle cx="10" cy="10" r="10" fill="#ffffff"/><rect x="5" y="6.5" width="10" height="7" fill="#d92629"/><path d="M5 6.5l5 4 5-4" fill="none" stroke="#ffffff" stroke-width="1"/></svg>
      marcus@hadleypartnersgroup.com
    </li>
    <li>
      <svg class="contact-icon" viewBox="0 0 20 20"><circle cx="10" cy="10" r="10" fill="#ffffff"/><path d="M10 5l5 4.5h-1.5V15h-7V9.5H5z" fill="#d92629"/></svg>
      42 W. Calloway St., Suite 300 Pasadena, CA 91417
    </li>
  </ul>

  <div class="holder">
    <p class="holder__name">Marcus J. Pellew</p>
    <p class="holder__title">President</p>
  </div>
</section>

<section class="card card--back" aria-label="Business card back">
  <svg class="card__art" viewBox="0 0 700 400" aria-hidden="true">
    <path d="M0,380 C230,250 470,160 700,140 L700,400 L0,400 Z" fill="#b9bbbd"/>
    <path d="M0,380 C230,250 470,160 700,140" fill="none" stroke="#d92629" stroke-width="6"/>
  </svg>
  <div class="wordmark wordmark--back"><span class="wordmark__square"></span>Hadley &amp; Partners</div>
  <p class="site-url">www.hadleypartnersgroup.com</p>
</section>

</body>
</html>
```